WordPress Site for Social Media Marketer

I would like a website designed and built on WordPress. It needs to have: About 10 pages
Need to integrate certain plugins like social media sites, FB Pixel tracking, etc.
A blog.
I need to have the ability to edit the site and make changes moving forward.
The site needs to have a look and feel similar to these:
https://www.lumenvault.co/
https://rosalindbrook.com/
https://www.nerinakowalczyk.com/

Target Market(s)

Coaches, Business Owners, some corporate clients (VIP)

Coding

Coded - Design and coding required

Number of Pages Required

1 page

Font styles to use
Serif
Sans Serif

Requirements
Must have
• Blog page
• List of clients
• List of work done. For an overview of what my current website looks like (whch should not be a guide at all), see www.celestemarlow.com
• The clients there are very high-profile, so I wan to highlight them, and some of the work done is very impressive, so we could use some of the social media images there if it helps.
• Needs to have an Snapfeed feed
Nice to have
• The look and feel needs to closely resemble these pages:
• https://www.lumenvault.co/
• https://rosalindbrook.com/
• https://www.livtorvelli.com/
Should not have
• Not sure what to do about colors. I am open to recommendations as long as the site is elegant, playful, modern, upscale, and feminine. Again, these sites are good reference points:
• https://www.brightmoorhub.co/

```html
<!DOCTYPE html>
<html lang="en">
<head>
<meta charset="utf-8">
<title>Lumenrise Social</title>
<link href="https://fonts.googleapis.com/css2?family=Questrial&family=Open+Sans:wght@400;600;700&display=swap" rel="stylesheet">
<style>
:root{
  --gold:#d9a53a;
  --ink:#243447;
  --text:#3a3a3a;
  --muted:#8a8a8a;
  --grey-band:#ececec;
  --white:#ffffff;
  --footer:#2b2b2b;
  --tooltip:#25364a;
  --footer-text:#dddddd;
  --link:#3a8fd0;
}
*{box-sizing:border-box;margin:0;padding:0}
html,body{width:1200px;height:3922px;overflow:hidden}
body{position:relative;background:var(--white);font-family:"Open Sans",Arial,sans-serif;color:var(--text)}
.abs{position:absolute}
.heading{position:absolute;left:0;width:1200px;text-align:center;font-family:"Questrial",Arial,sans-serif;font-weight:400;font-size:31px;letter-spacing:1px;color:var(--ink)}
.btn{position:absolute;background:var(--gold);color:var(--ink);font-family:"Questrial",Arial,sans-serif;display:flex;align-items:center;justify-content:center}

/* header */
.site-header{left:0;top:0;width:1200px;height:90px;background:var(--white)}
.brand{left:133px;top:31px;font-family:"Questrial",Arial,sans-serif;font-size:22px;color:var(--ink)}
.nav{left:488px;top:36px;display:flex;gap:28px;font-family:"Questrial",Arial,sans-serif;font-size:15px;color:var(--ink)}
.member{left:919px;top:25px;width:148px;height:40px;font-size:14px}

/* hero */
.hero{left:0;top:90px;width:1200px;height:525px;background:linear-gradient(120deg,#3a2a22 0%,#7a5a48 45%,#c8b2a0 70%,#5a4034 100%)}
.hero-title{left:133px;top:398px;font-family:"Questrial",Arial,sans-serif;font-weight:400;font-size:30px;line-height:40px;color:var(--white)}
.hero-btn{left:133px;top:485px;width:135px;height:45px;font-size:17px}
.arrow{top:335px;width:24px;height:34px}

/* services */
.service{top:740px;width:297px;height:225px}
.service .photo{width:100%;height:200px}
.service .label{position:absolute;left:15px;right:15px;bottom:0;height:45px;background:var(--gold);font-family:"Questrial",Arial,sans-serif;font-size:22px;color:var(--ink);display:flex;align-items:center;justify-content:center}

/* clients */
.band{left:0;width:1200px;background:var(--grey-band)}
.client{font-family:"Questrial",Arial,sans-serif;font-size:22px;color:var(--ink);width:230px;text-align:center}
.tooltip{left:133px;top:1258px;width:535px;height:40px;background:var(--tooltip);color:var(--white);font-size:14px;display:flex;align-items:center;justify-content:center;gap:12px}

/* blog */
.post-img{top:1588px;width:444px;height:310px}
.post-card{top:1858px;width:412px;height:200px;background:var(--white);box-shadow:0 1px 4px rgba(0,0,0,.12);padding:18px 24px}
.post-card h3{font-family:"Questrial",Arial,sans-serif;font-weight:400;font-size:19px;color:var(--ink)}
.post-card .date{font-size:12px;margin-top:10px;color:var(--text)}
.post-card p{font-size:10px;line-height:15px;color:var(--muted);margin-top:10px}
.post-card .more{position:static;margin-top:14px;width:96px;height:30px;font-size:13px}

/* works */
.work{background:var(--white);box-shadow:0 1px 3px rgba(0,0,0,.1);padding:16px 14px}
.work .who{display:flex;gap:10px;align-items:center}
.work .av{width:46px;height:46px;border-radius:50%;background:#f1f1f1;flex:none}
.work .name{font-family:"Questrial",Arial,sans-serif;font-size:15px;color:var(--ink)}
.work .meta{font-size:10px;color:var(--muted)}
.work p{font-size:12px;line-height:18px;margin-top:16px;color:var(--text)}
.work .media{margin-top:14px}
.work .link{color:var(--link)}
.view-all{left:550px;top:3095px;width:98px;height:30px;font-size:13px}

/* photo feed */
.feed{top:3330px;width:180px;height:153px}

/* cta */
.cta-text{left:0;top:3655px;width:1200px;text-align:center;font-family:"Questrial",Arial,sans-serif;font-size:22px;line-height:32px;color:var(--ink)}
.cta-btn{left:536px;top:3720px;width:128px;height:38px;font-size:15px}

/* footer */
.site-footer{left:0;top:3830px;width:1200px;height:92px;background:var(--footer)}
.foot-text{color:var(--footer-text);font-size:11px}
.foot-links{left:133px;top:3852px;display:flex;gap:10px}
.copy{left:133px;top:3882px}
.group{left:855px;top:3855px;width:143px;height:38px;border:1px solid #666;font-size:8px;line-height:11px;text-align:center;padding-top:7px;color:var(--footer-text)}
.social{top:3866px;width:14px;height:14px;border-radius:50%;background:var(--footer-text)}
</style>
</head>
<body>

<header class="abs site-header">
  <div class="abs brand">Lumenrise Social</div>
  <nav class="abs nav"><span>HOME</span><span>ABOUT</span><span>CLIENTS</span><span>SERVICES</span><span>CONTACT</span></nav>
  <div class="btn member">MEMBER LOGIN</div>
</header>

<section>
  <div class="abs hero" role="img" aria-label="Hand holding a smartphone with floating social reaction bubbles"></div>
  <svg class="abs arrow" style="left:45px" viewBox="0 0 24 34"><path d="M18 3 L5 17 L18 31" stroke="#fff" stroke-width="4" fill="none"/></svg>
  <svg class="abs arrow" style="left:1130px" viewBox="0 0 24 34"><path d="M6 3 L19 17 L6 31" stroke="#fff" stroke-width="4" fill="none"/></svg>
  <h1 class="abs hero-title">The Social Media Marketing Agency<br>of those Transforming Lives</h1>
  <div class="btn hero-btn">Contact Us</div>
</section>

<section>
  <h2 class="heading" style="top:686px">SERVICES</h2>
  <div class="abs service" style="left:133px"><div class="photo" role="img" aria-label="Tablet showing charts on a desk" style="background:linear-gradient(135deg,#bfc3c7,#6d7278)"></div><div class="label">Courses</div></div>
  <div class="abs service" style="left:451px"><div class="photo" role="img" aria-label="Phone with social notifications in hand" style="background:linear-gradient(135deg,#9aa0a6,#4a4f55)"></div><div class="label">In-Person Workshops</div></div>
  <div class="abs service" style="left:769px"><div class="photo" role="img" aria-label="Person working on laptop" style="background:linear-gradient(135deg,#8c9096,#3b3f45)"></div><div class="label">1-1 Help</div></div>
</section>

<section>
  <div class="abs band" style="top:1047px;height:408px"></div>
  <h2 class="heading" style="top:1118px">CLIENTS</h2>
  <div class="abs client" style="left:75px;top:1203px">Corvale Cola</div>
  <div class="abs client" style="left:323px;top:1203px">Fraveline</div>
  <div class="abs client" style="left:615px;top:1203px">Sollen Hill</div>
  <div class="abs client" style="left:885px;top:1203px">Whirlmont</div>
  <div class="abs tooltip"><span>Social Media Strategy</span>|<span>Content Creation</span>|<span>Reporting and Analytics</span></div>
  <div class="abs client" style="left:65px;top:1338px">Dellarose</div>
  <div class="abs client" style="left:323px;top:1338px">Voyara Company</div>
  <div class="abs client" style="left:615px;top:1338px">Marbeck Financial</div>
  <div class="abs client" style="left:880px;top:1338px">Tidewave Café</div>
</section>

<section>
  <h2 class="heading" style="top:1526px">BLOG</h2>
  <svg class="abs" style="left:55px;top:1730px" width="14" height="24" viewBox="0 0 14 24"><path d="M12 2 L3 12 L12 22" stroke="#999" stroke-width="2" fill="none"/></svg>
  <svg class="abs" style="left:1130px;top:1730px" width="14" height="24" viewBox="0 0 14 24"><path d="M2 2 L11 12 L2 22" stroke="#999" stroke-width="2" fill="none"/></svg>
  <div class="abs post-img" style="left:133px;background:linear-gradient(135deg,#5f8a4a,#e6d65a 50%,#3c4a2a)" role="img" aria-label="Notebook with content marketing sketch notes"></div>
  <div class="abs post-img" style="left:624px;background:linear-gradient(135deg,#e8e6df,#b9d36a 40%,#5aa7d8 70%,#d9dcd8)" role="img" aria-label="Desk with devices and connected social icons"></div>
  <article class="abs post-card" style="left:147px">
    <h3>Etiam mattis augue vehicula odio</h3>
    <div class="date">22 Sep, 2018</div>
    <p>Aliquam erat volutpat. Quisque aliquet ex nec est vestibulum pulvinar. Pellentesque convallis molestie enim sit amet efficitur. Etiam id imperdiet lectus. Vivamus lacus justo, ultrices nec erat.</p>
    <div class="btn more">Read More</div>
  </article>
  <article class="abs post-card" style="left:638px">
    <h3>Phasellus nisl est condimentum</h3>
    <div class="date">22 Sep, 2018</div>
    <p>Aliquam erat volutpat. Quisque aliquet ex nec est vestibulum pulvinar. Pellentesque convallis molestie enim sit amet efficitur. Etiam id imperdiet lectus. Vivamus lacus justo, ultrices nec erat.</p>
    <div class="btn more">Read More</div>
  </article>
</section>

<section>
  <div class="abs band" style="top:2140px;height:1065px"></div>
  <h2 class="heading" style="top:2210px">OUR WORKS</h2>

  <div class="abs work" style="left:133px;top:2270px;width:297px;height:300px">
    <div class="who"><div class="av"></div><div><div class="name">Sollen Hill</div><div class="meta">September 22, 2018</div></div></div>
    <p>Etiam mattis augue vehicula odio posuere</p>
    <div class="media" role="img" aria-label="Red wine pouring into glass" style="height:160px;background:linear-gradient(135deg,#1a1010,#8a1a14 60%,#2a0d0a)"></div>
  </div>
  <div class="abs work" style="left:133px;top:2585px;width:297px;height:295px">
    <div class="who"><div class="av"></div><div><div class="name">Whirlmont</div><div class="meta">@whirlmont</div></div></div>
    <p>Vivamus lacus justo, ultrices nec erat</p>
    <div class="media" role="img" aria-label="Man loading a washing machine" style="height:160px;background:linear-gradient(135deg,#2e3d52,#8aa0b8 55%,#3a4a5e)"></div>
  </div>
  <div class="abs work" style="left:133px;top:2910px;width:297px;height:160px">
    <div class="who"><div class="av"></div><div><div class="name">Corvale Cola</div><div class="meta">@corvalecola</div></div></div>
    <p>Maecenas vel tortor accumsan quam varius imperdiet vel eget elit. Aenean facilisis tinci-<span class="link">dunt lectus, id dictum nisl.</span></p>
  </div>

  <div class="abs work" style="left:451px;top:2270px;width:615px;height:480px">
    <div class="who"><div class="av"></div><div><div class="name">Fraveline</div><div class="meta">September 22, 2018</div></div></div>
    <p>Pellentesque convallis molestie enim sit amet efficitur. Etiam id imperdiet lectus</p>
    <div class="media" role="img" aria-label="Video still of a liqueur bottle on a wooden table" style="height:340px;background:linear-gradient(135deg,#6b4a22,#d9a83c 50%,#7a5a38);position:relative">
      <svg style="position:absolute;left:268px;top:145px" width="50" height="50" viewBox="0 0 50 50"><circle cx="25" cy="25" r="23" fill="none" stroke="#fff" stroke-width="3"/><path d="M20 15 L35 25 L20 35 Z" fill="#fff"/></svg>
    </div>
  </div>
  <div class="abs work" style="left:451px;top:2768px;width:297px;height:287px">
    <div class="who"><div class="av"></div><div><div class="name">Voyara Company</div><div class="meta">September 22, 2018</div></div></div>
    <p>Cras augue magna, placerat ege</p>
    <div class="media" role="img" aria-label="Modern villa with pool under blue sky" style="height:160px;background:linear-gradient(180deg,#7fb4e0,#e8eef2 55%,#2f8fc6)"></div>
  </div>
  <div class="abs work" style="left:769px;top:2768px;width:297px;height:287px">
    <div class="who"><div class="av"></div><div><div class="name">Tidewave Smoothie Café</div><div class="meta">@tidewavecafe</div></div></div>
    <p>Fusce vitae lectus sit amet mi pulvinar</p>
    <div class="media" role="img" aria-label="Cups of latte art from above" style="height:160px;background:linear-gradient(135deg,#6a3e1c,#d9a66a 50%,#4a2a14)"></div>
  </div>
  <div class="btn view-all">View All</div>
</section>

<section>
  <h2 class="heading" style="top:3278px">SNAPFEED</h2>
  <div class="abs feed" style="left:133px;background:linear-gradient(135deg,#3aa0d8,#e89040)" role="img" aria-label="Colourful action sports shot"></div>
  <div class="abs feed" style="left:322px;background:linear-gradient(180deg,#e8c070,#c88a3a)" role="img" aria-label="Camel caravan in desert dunes"></div>
  <div class="abs feed" style="left:511px;background:linear-gradient(135deg,#2a1a12,#7a4a2a)" role="img" aria-label="Cigars on dark surface"></div>
  <div class="abs feed" style="left:700px;background:linear-gradient(180deg,#d89a5a,#4a2a1a)" role="img" aria-label="Palm trees at sunset"></div>
  <div class="abs feed" style="left:889px;width:177px;background:linear-gradient(135deg,#d85a3a,#e8c04a 50%,#6a4a2a)" role="img" aria-label="Bottles of fresh juices in a crate"></div>
</section>

<section>
  <div class="abs band" style="top:3565px;height:265px"></div>
  <p class="abs cta-text">Get my cheat sheet on how to get unstuck<br>when you don’t know what to post on social media!</p>
  <div class="btn cta-btn">Subscribe Now</div>
</section>

<footer>
  <div class="abs site-footer"></div>
  <div class="abs foot-links foot-text"><span>Home</span>|<span>About</span>|<span>Clients</span>|<span>Services</span>|<span>Contact</span>|<span>Member Login</span>|<span>Blog</span>|<span>Privacy Policy</span></div>
  <div class="abs copy foot-text">Copyright © 2018 Lumenrise Social. All rights reserved.</div>
  <div class="abs group">Join our free Social Media<br>Mastery Circle Group</div>
  <div class="abs social" style="left:1016px"></div>
  <div class="abs social" style="left:1046px"></div>
</footer>

</body>
</html>
```